Business Card Design

My business is writing crime novels to entertain readers. I write legal thrillers and mysteries. I need a card for publishers, agents, other authors, and media.

Industry/Entity Type

Legal

Contact Information for Business Card

Paul Ostrander
www.ostranderthrillers.example
paulbostrander@mailbox.example
0064 27 5139427

```html
<!DOCTYPE html>
<html lang="en">
<head>
<meta charset="utf-8">
<title>Paul Ostrander – Business Card</title>
<link rel="stylesheet" href="https://fonts.googleapis.com/css2?family=Oswald:wght@500&family=Arimo:wght@400&display=swap">
<style>
  :root {
    --page-bg: #ffffff;
    --card-gold: #b07b2c;
    --card-gold-soft: #c2924a;
    --card-grey: #e8e9ea;
    --card-edge: #a9a9a9;
    --text-light: #ffffff;
  }

  * { margin: 0; padding: 0; box-sizing: border-box; }

  html, body {
    width: 1200px;
    height: 876px;
    overflow: hidden;
    background: var(--page-bg);
  }

  .canvas {
    position: relative;
    width: 1200px;
    height: 876px;
  }

  .business-card {
    position: absolute;
    left: 184px;
    top: 192px;
    width: 824px;
    height: 485px;
    border: 2px solid var(--card-edge);
    display: flex;
    overflow: hidden;
  }

  .identity-panel {
    position: relative;
    width: 440px;
    height: 100%;
    background: var(--card-gold);
    color: var(--text-light);
  }

  .author-name {
    position: absolute;
    left: 56px;
    top: 190px;
    font-family: "Oswald", "Arial Narrow", sans-serif;
    font-weight: 500;
    font-size: 38px;
    line-height: 1;
    letter-spacing: 0.2px;
    white-space: nowrap;
  }

  .contact-list {
    position: absolute;
    left: 56px;
    top: 273px;
    list-style: none;
    font-family: "Arimo", Helvetica, Arial, sans-serif;
    font-size: 21px;
    line-height: 1;
    white-space: nowrap;
  }

  .contact-list li { height: 52px; }

  .portrait-panel {
    flex: 1;
    height: 100%;
    background: var(--card-grey);
  }

  .portrait-panel svg {
    display: block;
    width: 100%;
    height: 100%;
  }
</style>
</head>
<body>
  <div class="canvas">
    <section class="business-card">
      <div class="identity-panel">
        <h1 class="author-name">Paul Ostrander</h1>
        <ul class="contact-list">
          <li class="contact-web">www.ostranderthrillers.example</li>
          <li class="contact-email">paulbostrander@mailbox.example</li>
          <li class="contact-phone">0064 27 5139427</li>
        </ul>
      </div>
      <div class="portrait-panel">
        <svg role="img" aria-label="Two-tone gold stencil portrait of the author in glasses, resting his chin on his hand" viewBox="0 0 380 481" preserveAspectRatio="none">
          <defs>
            <radialGradient id="portrait-tone" cx="0.78" cy="0.55" r="0.7" fx="0.82" fy="0.6">
              <stop offset="0" stop-color="#b07b2c"/>
              <stop offset="0.4" stop-color="#c2924a"/>
              <stop offset="0.75" stop-color="#dcd2c2"/>
              <stop offset="1" stop-color="#e8e9ea"/>
            </radialGradient>
          </defs>
          <rect width="380" height="481" fill="#e8e9ea"/>
          <rect width="380" height="481" fill="url(#portrait-tone)"/>
        </svg>
      </div>
    </section>
  </div>
</body>
</html>
```